Re-Design landingpage of a productive wordpress website

The task is to re-design the landing page of www.portal.unsertk.de
The landing page displays a bunch of possibilities for the users to interact with their city (content area).
In the widget area there are some links to additional information.
What I do not like on the current site:
- It is just a list, there is no center, there is no focus to look on...
- The elements are not aligned on top
- The proportions are wrong, there is no golden section

colours, fonts ... are given by the CI, so they should not be changed

We would like you to apply with a psd-layout proposal.
Please only apply if you are able to realize the design in wordpress (with content boxes as custom post types) for a fixed price of additional 150 €

```html
<!DOCTYPE html>
<html lang="de">
<head>
<meta charset="utf-8">
<title>UnserTK.de – gemeinsam Stadt bewegen</title>
<link rel="stylesheet" href="https://fonts.googleapis.com/css2?family=Arimo:wght@400;700&display=swap">
<style>
:root{
  --lime:#cfcc00;
  --lime-soft:#d9d84c;
  --olive:#8f9a00;
  --olive-text:#a3ab00;
  --ink:#1d1d1d;
  --muted:#777;
  --panel:#ececec;
  --panel-light:#f4f4f4;
  --white:#fff;
  --line:#d2d2d2;
  --footer:#43a9ec;
  --accent-blue:#2a98d8;
}
*{box-sizing:border-box;margin:0;padding:0}
html,body{width:728px;height:1200px;overflow:hidden}
body{position:relative;font-family:"Arimo",Arial,sans-serif;color:var(--ink);background:var(--white)}
.abs{position:absolute}
.backdrop{left:0;top:0;width:728px;height:1141px;
  background:linear-gradient(180deg,#4aa8ec 0%,#8fcaf3 22%,#c9dce6 40%,#a9a69a 55%,#d8d6cf 75%,#eceae4 100%)}
.brand{left:120px;top:14px;display:flex;align-items:center;gap:7px}
.brand-dot{width:26px;height:26px;border-radius:50%;background:#f2d21a}
.brand-name{font-size:11px;color:#333;letter-spacing:.3px}
.search{left:449px;top:15px;width:151px;height:23px;border:1px solid #9bb0c0;background:var(--white)}
.search-btn{position:absolute;right:-1px;top:-1px;width:25px;height:23px;background:var(--accent-blue);display:flex;align-items:center;justify-content:center}
.hero{left:108px;top:65px;width:513px;height:225px;background:var(--lime)}
.hero-title{position:absolute;left:0;right:0;top:25px;text-align:center;line-height:1;color:#222}
.hero-title .name{font-size:27px;font-weight:700;display:block;letter-spacing:-.3px}
.hero-title .claim{font-size:11.5px;font-weight:400;display:block;margin-top:4px}
.quote-panel{position:absolute;left:12px;top:84px;width:488px;height:114px;background:var(--lime-soft)}
.portrait{position:absolute;left:56px;top:9px;width:95px;height:95px;border-radius:50%;border:3px solid var(--white);
  background:radial-gradient(circle at 50% 45%,#e6d2c4 0%,#b7a597 60%,#cfcc00 100%)}
.quote-mark{position:absolute}
.quote-open{left:191px;top:15px}
.quote-close{left:420px;top:55px}
.quote-text{position:absolute;left:212px;top:30px;width:220px;font-size:9.8px;line-height:12px;color:#222}
.quote-author{position:absolute;left:212px;top:81px;font-size:14px;color:#222}
.dots{position:absolute;left:425px;top:98px;display:flex;gap:4px}
.dots span{width:9px;height:9px;border-radius:50%;background:#ebebd5}
.dots span.on{background:#5bb7ea}
.mainnav{left:108px;top:290px;width:513px;height:34px;background:linear-gradient(#fff,#f3f3f3);border-bottom:1px solid var(--line);
  display:flex;align-items:center;justify-content:center;gap:10px;font-size:10px;color:#222}
.mainnav .sep{color:#444}
.content{left:108px;top:324px;width:513px;height:644px;background:var(--panel)}
.section-head{position:absolute;left:0;right:0;text-align:center}
.section-head h1{font-size:14.5px;font-weight:400;letter-spacing:.3px}
.section-head p{font-size:8.5px;color:var(--olive);margin-top:4px;letter-spacing:.3px}
.card{position:absolute;top:91px;width:139px;height:201px;background:var(--white);box-shadow:0 4px 4px -2px rgba(0,0,0,.15);text-align:center}
.card-media{height:74px}
.card h2{font-size:8px;font-weight:400;color:var(--olive-text);margin-top:12px;letter-spacing:.2px}
.card h2::after{content:"";display:block;width:30px;height:1.5px;background:var(--olive-text);margin:3px auto 0}
.card h3{font-size:7.5px;font-weight:400;color:var(--olive-text);margin-top:8px;line-height:9px}
.card p{font-size:6.2px;color:var(--muted);line-height:10px;margin:3px 6px 0}
.events{left:120px;top:648px;width:486px;height:286px;background:var(--white);border:1px solid #d8d8d8}
.event{position:absolute;width:230px;height:65px}
.event-media{position:absolute;left:0;top:0;width:81px;height:65px;border:1px solid #ddd}
.event-body{position:absolute;left:92px;top:0;width:128px}
.event-body h4{font-size:7.5px;font-weight:400;color:#222}
.event-body p{font-size:6px;line-height:7.6px;color:#888;margin-top:3px}
.event-body a{display:block;font-size:6.2px;color:var(--olive-text);margin-top:5px;text-decoration:none}
.rule{position:absolute;height:1px;width:218px;background:var(--line)}
.news{left:108px;top:968px;width:513px;height:173px;background:var(--panel-light)}
.news h1{position:absolute;left:0;right:0;top:25px;text-align:center;font-size:14.5px;font-weight:400;letter-spacing:.4px}
.news-item{position:absolute;top:55px;width:105px}
.news-media{height:57px;border:1px solid #ccd}
.news-item h5{font-size:8px;font-weight:400;margin-top:5px}
.news-item .by{font-size:6.5px;color:var(--olive-text);margin-top:1px}
.news-item .meta{font-size:5.5px;color:#999;margin-top:4px}
.footer{left:0;top:1141px;width:728px;height:59px;background:var(--footer);display:flex;align-items:center;justify-content:center;gap:8px;font-size:6.5px;color:var(--white)}
</style>
</head>
<body>
<div class="abs backdrop" role="img" aria-label="Blurred view of a palace courtyard under a blue sky"></div>

<div class="abs brand"><span class="brand-dot"></span><span class="brand-name">TALSTADT</span></div>
<div class="abs search"><span class="search-btn">
  <svg width="13" height="13" viewBox="0 0 13 13"><circle cx="5" cy="5" r="3.6" fill="none" stroke="#fff" stroke-width="1.6"/><line x1="7.6" y1="7.6" x2="11.8" y2="11.8" stroke="#fff" stroke-width="2"/></svg>
</span></div>

<header class="abs hero">
  <div class="hero-title"><span class="name">UnserTK.de</span><span class="claim">gemeinsam Stadt bewegen</span></div>
  <div class="quote-panel">
    <div class="portrait" role="img" aria-label="Portrait photo of a young woman with glasses"></div>
    <svg class="quote-mark quote-open" width="20" height="16" viewBox="0 0 20 16"><g fill="#222"><circle cx="4.5" cy="11" r="4.2"/><path d="M1 11 Q1 3 7 0 L8 1.5 Q4 4 3.5 9Z"/><circle cx="14.5" cy="11" r="4.2"/><path d="M11 11 Q11 3 17 0 L18 1.5 Q14 4 13.5 9Z"/></g></svg>
    <p class="quote-text">Ich mochte wissen, was in jungen Menschen Vorgeht und ihnen vermitteln, wie sie etwas bewegen konnen. Deshalb bringe ich mich ein.“</p>
    <svg class="quote-mark quote-close" width="20" height="16" viewBox="0 0 20 16"><g fill="#222" transform="rotate(180 10 8)"><circle cx="4.5" cy="11" r="4.2"/><path d="M1 11 Q1 3 7 0 L8 1.5 Q4 4 3.5 9Z"/><circle cx="14.5" cy="11" r="4.2"/><path d="M11 11 Q11 3 17 0 L18 1.5 Q14 4 13.5 9Z"/></g></svg>
    <p class="quote-author">Lena Moor, Weststadt</p>
    <div class="dots"><span class="on"></span><span></span><span></span><span></span><span></span></div>
  </div>
</header>

<nav class="abs mainnav">
  <span>Beteiligung</span><span class="sep">|</span><span>Jugendhearing</span><span class="sep">|</span><span>Ideen/ Projekte</span><span class="sep">|</span><span>Frag-den-OB</span><span class="sep">|</span><span>STEP</span><span class="sep">|</span><span>Mängelmeldung</span>
</nav>

<main class="abs content">
  <div class="section-head" style="top:30px"><h1>LOREM IPSUM DOLOR SIT AMET</h1><p>ALIQUAM TINCIDUNT MAURIS EU RISUS.</p></div>

  <article class="card" style="left:30px">
    <div class="card-media" role="img" aria-label="Group of smiling people giving thumbs up" style="background:linear-gradient(90deg,#d8c8bc,#3aa7a0 35%,#e06aa0 60%,#7a7a8a)"></div>
    <h2>EHRENAMT</h2>
    <h3>BÜRGERSCHAFTLICHES<br>ENGAGEMENT</h3>
    <p>Sie haben Interesse an einer freiwilligen Tätigkeit? Wir helfen Ihnen, das Richtige zu finden. Sehen Sie nach, wo Hilfe gesucht wird.</p>
  </article>
  <article class="card" style="left:188px">
    <div class="card-media" role="img" aria-label="Bricks, hard hat and rolled construction plans" style="background:linear-gradient(90deg,#e9875a,#f2a52a 45%,#e8e8ea 70%,#f4f4f4)"></div>
    <h2>STADTENTWICKLUNGSPLÄNE</h2>
    <h3>BÜRGERSCHAFTLICHES<br>ENGAGEMENT</h3>
    <p>Die Stadtteilentwicklungspläne (STEPs) sind Teil des Stadtentwicklungskonzepts. In ihnen werden die Leitsätze und strategischen Ziele des Stadtentwicklungskonzepts auf den jeweiligen Stadtteil heruntergebrochen und konkretisiert.</p>
  </article>
  <article class="card" style="left:347px">
    <div class="card-media" role="img" aria-label="Volunteers working outdoors by a stream" style="background:linear-gradient(160deg,#6b7a4a,#8a7a5a 50%,#4a5a3a)"></div>
    <h2>LOKALE AGENDA 21</h2>
    <h3>BÜRGERSCHAFTLICHES<br>ENGAGEMENT</h3>
    <p>Bei der Lokalen Agenda 21 entwickeln Bürgerinnen und Bürger, Gemeinderat und Stadtverwaltung in enger Abstimmung schrittweise nachhaltige Projekte und setzen diese zielstrebig um.</p>
  </article>
</main>

<section class="abs events">
  <div class="event" style="left:18px;top:19px">
    <div class="event-media" role="img" aria-label="Young people looking at their phones" style="background:linear-gradient(135deg,#8a7a70,#c9b5a5 50%,#5a5a6a)"></div>
    <div class="event-body"><h4>JUGENDHEARING 2015</h4><p>Am 20.03.2015 fand ein Jugendhearing statt. Die Teilnehmerinnen und Teilnehmer werden dessen Ergebnisse auf der Zukunftskonferenz vorstellen</p><a>Zu den Ergebnissen des Jugendhearings</a></div>
  </div>
  <div class="event" style="left:251px;top:19px">
    <div class="event-media" role="img" aria-label="Young people looking at their phones" style="background:linear-gradient(135deg,#8a7a70,#c9b5a5 50%,#5a5a6a)"></div>
    <div class="event-body"><h4>JUGENDHEARING 2015</h4><p>Am 20.03.2015 fand ein Jugendhearing statt. Die Teilnehmerinnen und Teilnehmer werden dessen Ergebnisse auf der Zukunftskonferenz vorstellen</p><a>Zu den Ergebnissen des Jugendhearings</a></div>
  </div>
  <div class="rule" style="left:18px;top:96px"></div><div class="rule" style="left:251px;top:96px"></div>

  <div class="event" style="left:18px;top:108px">
    <div class="event-media" role="img" aria-label="Pinned note with handwritten event slogan" style="background:#f7e9a4"></div>
    <div class="event-body"><h4>ZUKUNFTSKONFERENZ 2015</h4><p>Am 17. und 18. April 2015 treffen sich wieder engagierte Bürgerinnen und Bürger im Reithaus, um die zukünftige Stadtentwicklung mit Politik und Verwaltung zu diskutieren. Weitere Informationen folgen.</p><a>Start: 17.-18.04.2015</a></div>
  </div>
  <div class="event" style="left:251px;top:108px">
    <div class="event-media" role="img" aria-label="Pinned note with handwritten event slogan" style="background:#f7e9a4"></div>
    <div class="event-body"><h4>ZUKUNFTSKONFERENZ 2015</h4><p>Am 17. und 18. April 2015 treffen sich wieder engagierte Bürgerinnen und Bürger im Reithaus, um die zukünftige Stadtentwicklung mit Politik und Verwaltung zu diskutieren. Weitere Informationen folgen.</p><a>Start: 17.-18.04.2015</a></div>
  </div>
  <div class="rule" style="left:18px;top:186px"></div><div class="rule" style="left:251px;top:186px"></div>

  <div class="event" style="left:18px;top:199px">
    <div class="event-media" role="img" aria-label="Pinned note with handwritten event slogan" style="background:#f7e9a4"></div>
    <div class="event-body"><h4>ZUKUNFTSKONFERENZ 2015</h4><p>Am 17. und 18. April 2015 treffen sich wieder engagierte Bürgerinnen und Bürger im Reithaus, um die zukünftige Stadtentwicklung mit Politik und Verwaltung zu diskutieren. Weitere Informationen folgen.</p><a>Start: 17.-18.04.2015</a></div>
  </div>
  <div class="event" style="left:251px;top:199px">
    <div class="event-media" role="img" aria-label="Pinned note with handwritten event slogan" style="background:#f7e9a4"></div>
    <div class="event-body"><h4>ZUKUNFTSKONFERENZ 2015</h4><p>Am 17. und 18. April 2015 treffen sich wieder engagierte Bürgerinnen und Bürger im Reithaus, um die zukünftige Stadtentwicklung mit Politik und Verwaltung zu diskutieren. Weitere Informationen folgen.</p><a>Start: 17.-18.04.2015</a></div>
  </div>
</section>

<section class="abs news">
  <h1>NEWS STADTENTWICKLUNG</h1>
  <div class="news-item" style="left:23px"><div class="news-media" role="img" aria-label="Close-up of two hands holding" style="background:linear-gradient(135deg,#dfe6f2,#e8b9a4 55%,#d9e2ef)"></div><h5>Lorem ipsum dolor sit.</h5><p class="by">from Clara Wend</p><p class="meta">3 hours ago. 1200 views</p></div>
  <div class="news-item" style="left:140px"><div class="news-media" role="img" aria-label="Close-up of two hands holding" style="background:linear-gradient(135deg,#dfe6f2,#e8b9a4 55%,#d9e2ef)"></div><h5>Lorem ipsum dolor sit.</h5><p class="by">from Clara Wend</p><p class="meta">3 hours ago. 1200 views</p></div>
  <div class="news-item" style="left:258px"><div class="news-media" role="img" aria-label="Close-up of two hands holding" style="background:linear-gradient(135deg,#dfe6f2,#e8b9a4 55%,#d9e2ef)"></div><h5>Lorem ipsum dolor sit.</h5><p class="by">from Clara Wend</p><p class="meta">3 hours ago. 1200 views</p></div>
  <div class="news-item" style="left:375px"><div class="news-media" role="img" aria-label="Close-up of two hands holding" style="background:linear-gradient(135deg,#dfe6f2,#e8b9a4 55%,#d9e2ef)"></div><h5>Lorem ipsum dolor sit.</h5><p class="by">from Clara Wend</p><p class="meta">3 hours ago. 1200 views</p></div>
</section>

<footer class="abs footer"><span>Impressum und Datenschutz</span><span>|</span><span>Bildnachweise</span></footer>
</body>
</html>
```